Business Card Design for new social media business

I am looking for a new professional business card design for an exciting new company which is based on providing members with experiences of others to benefit their choice of places to visit for restaurants, bars, clubs, national monument, tourist sights, hotels and so forth.
Updates

Please submit designs as I will choose to commit the funds depending on designs.

Reason: More designs required

Target Market(s)

Business Managers as well as directors alongside owners

Industry/Entity Type

Business

Requirements
Must have
• Logo design and symbols
Nice to have
• Logo / Symbol on the back of the business card and possibly the logo as if embedded/embossed on the business card.

```html
<!DOCTYPE html>
<html lang="en">
<head>
<meta charset="UTF-8">
<title>ViewTrail Business Card</title>
<link href="https://fonts.googleapis.com/css2?family=Open+Sans:wght@400;600;700&display=swap" rel="stylesheet">
<style>
  :root {
    --bg: #2b2b2d;
    --card-white: #ffffff;
    --card-grey: #eeeeef;
    --brand-blue: #1f5fbf;
    --blue-light: #1f73d6;
    --blue-deep: #1a2c86;
    --accent-orange: #e0621c;
    --band-yellow: #f2b400;
    --band-orange: #c9601a;
    --text-dark: #2a2a2a;
    --watermark: rgba(0, 0, 0, 0.04);
  }
  * { margin: 0; padding: 0; box-sizing: border-box; }
  html, body {
    width: 1200px; height: 900px; overflow: hidden;
    background: var(--bg);
    font-family: "Open Sans", Arial, sans-serif;
  }
  .canvas {
    position: relative; width: 1200px; height: 900px;
    display: flex; flex-direction: column; align-items: center; justify-content: center; gap: 48px;
  }
  .card {
    position: relative; width: 630px; height: 360px; overflow: hidden;
    box-shadow: 0 10px 30px rgba(0,0,0,0.45);
  }

  /* Front */
  .card-front {
    background: linear-gradient(120deg, var(--card-white) 40%, var(--card-grey) 100%);
  }
  .front-watermark {
    position: absolute; right: 40px; top: -60px;
    width: 380px; height: 380px; border-radius: 50%;
    background: var(--watermark);
  }
  .brand-name {
    position: absolute; left: 38px; top: 42px;
    font-size: 50px; font-weight: 700; letter-spacing: -1px;
    color: var(--brand-blue);
  }
  .person { position: absolute; left: 56px; top: 150px; }
  .person-name {
    font-size: 23px; font-weight: 400; letter-spacing: 1px;
    color: var(--accent-orange); text-transform: uppercase;
  }
  .person-title { font-size: 17px; color: var(--text-dark); margin-top: 2px; }
  .contact-list { list-style: none; margin-top: 26px; }
  .contact-list li {
    display: flex; align-items: center; gap: 10px;
    font-size: 19px; color: var(--text-dark); line-height: 1.45;
  }
  .icon { width: 14px; height: 16px; flex: none; }
  .address {
    position: absolute; left: 390px; top: 158px;
    display: flex; gap: 8px; font-size: 18px; color: var(--text-dark); line-height: 1.35;
  }
  .address .icon { margin-top: 4px; }
  .bottom-band {
    position: absolute; left: 0; right: 0; bottom: 0; height: 28px;
    background: linear-gradient(90deg, var(--band-yellow), var(--band-orange));
  }

  /* Back */
  .card-back {
    background: radial-gradient(circle at 55% 45%, var(--blue-light) 0%, var(--brand-blue) 40%, var(--blue-deep) 100%);
  }
  .back-url {
    position: absolute; left: 30px; bottom: 30px;
    transform-origin: left bottom; transform: rotate(-90deg) translateY(100%);
    font-size: 17px; color: var(--card-white); letter-spacing: 0.5px;
  }
  .back-mark {
    position: absolute; inset: 0;
    display: flex; align-items: center; justify-content: center; gap: 18px;
  }
  .back-mark .dot {
    width: 54px; height: 54px; border-radius: 50%; background: var(--band-yellow);
  }
  .back-mark .name {
    font-size: 58px; font-weight: 700; letter-spacing: -1px; color: var(--card-white);
  }
</style>
</head>
<body>
<main class="canvas">
  <section class="card card-front" aria-label="Business card front">
    <div class="front-watermark"></div>
    <div class="brand-name">ViewTrail</div>

    <div class="person">
      <div class="person-name">Mira Holloway</div>
      <div class="person-title">managing director</div>
      <ul class="contact-list">
        <li>
          <svg class="icon" viewBox="0 0 14 16" aria-hidden="true">
            <rect x="3" y="0.5" width="8" height="15" rx="1.5" fill="none" stroke="var(--accent-orange)" stroke-width="1.6"/>
            <circle cx="7" cy="12.8" r="0.9" fill="var(--accent-orange)"/>
          </svg>
          888 888 88 88
        </li>
        <li>
          <svg class="icon" viewBox="0 0 14 16" aria-hidden="true">
            <rect x="0" y="4" width="14" height="9" fill="var(--accent-orange)"/>
            <path d="M0 4 L7 9.5 L14 4" fill="none" stroke="#fff" stroke-width="1.2"/>
          </svg>
          mholloway@viewtrail.com
        </li>
      </ul>
    </div>

    <div class="address">
      <svg class="icon" viewBox="0 0 14 16" aria-hidden="true">
        <path d="M7 16 C7 16 1 9.5 1 6 A6 6 0 0 1 13 6 C13 9.5 7 16 7 16Z" fill="var(--accent-orange)"/>
        <circle cx="7" cy="6" r="2.2" fill="#fff"/>
      </svg>
      <div>123 Fake Street<br>Anytown, New York 12345</div>
    </div>

    <div class="bottom-band"></div>
  </section>

  <section class="card card-back" aria-label="Business card back">
    <div class="back-url">www.viewtrail.com</div>
    <div class="back-mark">
      <span class="dot"></span>
      <span class="name">ViewTrail</span>
    </div>
  </section>
</main>
</body>
</html>
```